Collectibles expert needs a new business card design.

My current business card makes me look to high end. It may even make me look arrogant or too stuffy. I do work with high end clients and their items but most of my business is with average people with average items. My business name is Walter Brennick's Oak Lane Digging Co. The idea was that I mine the streets helping people discover the treasures buried in their homes. That could be art, jewelry, coins, etc. The name and an older logo I used does not make immediate sense to most people. I tried to go with just my picture and name and that is the current card I am changing. I help people who need to downsize. Whether they are getting rid of one item, a collection or a house full of items I help them discover what they have, what it is worth and what are the best ways we can get the most for them. This may be a combination of estate sale (which I dont do) auction or sell directly to a dealer or collector. Usually it is a combination of these. My main goal is to help make sure they dont accidently sell a Vantorre painting in a garage sale. I am uploading a copy of my old card and the old logo I used to use but the winning card design will need to be much different than these. You can learn a little more about me at www.walterpbrennick.com, www.oaklanedigin.com and www.facebook.com/oldco. I hope someone can look at what I do and come up with a very unique design that will be equally effective if my client is high income or if my client is low to mid income. I do not care if it is a one or two sided card as long as it conveys my contact information and a good representation of what I do.

Target Market(s)

People who are getting rid of items. These can be elderly couples or individuals that are moving to an active living community and will have less space so they need to sell items. This can also include the children of elder parents that dont want their stuff and want to find solutions to help them get rid of their items.

Contact Information for Business Card

The card should have my business name Walter Brennick's Oak Lane Digging Co., phone number 555-382-19073, email walter@oaklanedigging.com and website www.oaklanedigging.com. Would also like to include Buyer, Broker, Consultant and Appraiser. We can put Walter P. Brennick, ISA on the opposite side of the company name since it includes my name as well.

Font styles to use
Sans Serif

Colors

Designer to choose colors to be used in the design.

Requirements
Must have
• My project must have a professional look. It must not alienate low income clients and should still be appealing to high value clients.

```html
<!DOCTYPE html>
<html lang="en">
<head>
<meta charset="utf-8">
<title>Walter Brennick's Oak Lane Digging Co – Business Card</title>
<link href="https://fonts.googleapis.com/css2?family=Nunito:wght@300;800&family=Open+Sans:wght@400;600&display=swap" rel="stylesheet">
<style>
  :root {
    --page: #e9e4dc;
    --tan: #a89474;
    --tan-light: #c2ad8b;
    --brown: #3a2f28;
    --brown-soft: #4a3d34;
    --cream: #f6f1e8;
    --art-red: #7a3b2e;
    --art-blue: #7fa6c9;
  }
  * { box-sizing: border-box; margin: 0; padding: 0; }
  html, body { width: 1200px; height: 1200px; overflow: hidden; }
  body {
    background: var(--page);
    font-family: "Open Sans", sans-serif;
    position: relative;
  }
  .card {
    position: absolute;
    left: 160px;
    width: 880px;
    height: 503px;
    overflow: hidden;
    box-shadow: 0 10px 30px rgba(40, 30, 20, .25);
  }
  .card--front { top: 60px; background: var(--tan); }
  .card--back { top: 637px; background: var(--brown); }

  /* front */
  .corner-bracket { position: absolute; }
  .front-bracket { left: 150px; top: 40px; }
  .front-art {
    position: absolute; left: 150px; top: 95px; width: 250px; height: 185px;
    border-radius: 6px;
    background: linear-gradient(120deg, var(--art-red) 0 45%, var(--art-blue) 60% 100%);
  }
  .identity { position: absolute; left: 470px; top: 225px; color: var(--brown); }
  .identity__name { font-family: "Nunito", sans-serif; font-weight: 800; font-size: 40px; line-height: 1.05; }
  .identity__company { font-family: "Nunito", sans-serif; font-weight: 300; font-size: 32px; line-height: 1.15; }
  .contact-list { position: absolute; left: 440px; top: 330px; list-style: none; color: var(--brown); }
  .contact-list li {
    display: flex; align-items: center; gap: 8px;
    font-size: 19px; font-weight: 600; line-height: 30px;
  }
  .contact-list svg { width: 20px; height: 20px; flex: none; }
  .front-band {
    position: absolute; left: 0; right: 0; top: 420px; bottom: 0; background: var(--brown);
  }
  .front-stripe {
    position: absolute; left: 0; right: 0; height: 8px; background: var(--tan);
  }
  .front-stripe--one { top: 432px; }
  .front-stripe--two { top: 452px; left: 560px; }
  .services {
    position: absolute; left: 28px; top: 440px;
    border: 2px solid var(--cream); color: var(--cream);
    padding: 6px 14px; font-size: 20px; line-height: 1.2; background: var(--brown);
  }

  /* back */
  .back-art {
    position: absolute; left: 90px; top: 40px; width: 230px; height: 290px;
    border-radius: 6px; opacity: .35;
    background: linear-gradient(160deg, var(--tan-light), var(--brown-soft));
  }
  .back-bracket { left: 80px; top: 250px; }
  .name-pill {
    position: absolute; left: 410px; right: 0; top: 150px; height: 130px;
    background: var(--tan); border-radius: 65px 0 0 65px;
    padding: 18px 0 0 46px; color: var(--brown);
  }
  .name-pill .identity__name { font-size: 42px; }
  .name-pill .identity__company { font-size: 33px; }
  .web-box {
    position: absolute; left: 470px; top: 375px;
    border: 2px solid var(--tan); color: var(--tan);
    padding: 6px 14px; font-size: 19px;
    display: flex; align-items: center; gap: 8px;
  }
  .web-box svg { width: 18px; height: 18px; }
</style>
</head>
<body>

<section class="card card--front" aria-label="Business card front">
  <svg class="corner-bracket front-bracket" width="120" height="50" viewBox="0 0 120 50" aria-hidden="true">
    <polyline points="2,48 2,2 118,2" fill="none" stroke="var(--brown)" stroke-width="3"/>
  </svg>
  <div class="front-art" role="img" aria-label="Illustration of a pin-up miner with a pickaxe sitting on an ore cart filled with gold"></div>

  <div class="identity">
    <div class="identity__name">Walter Brennick's</div>
    <div class="identity__company">Oak Lane Digging Co</div>
  </div>

  <ul class="contact-list">
    <li>
      <svg viewBox="0 0 20 20" aria-hidden="true"><circle cx="10" cy="10" r="9.5" fill="var(--brown)"/><path d="M7 5.5l2 2-1 1.2a6 6 0 0 0 3.3 3.3l1.2-1 2 2-1.3 1.5C9.5 14.5 5.5 10.5 5.5 6.8z" fill="var(--tan)"/></svg>
      555-382-19073
    </li>
    <li>
      <svg viewBox="0 0 20 20" aria-hidden="true"><circle cx="10" cy="10" r="9.5" fill="var(--brown)"/><rect x="5" y="6.5" width="10" height="7" fill="none" stroke="var(--tan)" stroke-width="1.4"/><polyline points="5,6.5 10,10.5 15,6.5" fill="none" stroke="var(--tan)" stroke-width="1.4"/></svg>
      walter@oaklanedigging.com
    </li>
    <li>
      <svg viewBox="0 0 20 20" aria-hidden="true"><circle cx="10" cy="10" r="9.5" fill="var(--brown)"/><circle cx="10" cy="10" r="5.5" fill="none" stroke="var(--tan)" stroke-width="1.2"/><ellipse cx="10" cy="10" rx="2.3" ry="5.5" fill="none" stroke="var(--tan)" stroke-width="1.2"/><line x1="4.5" y1="10" x2="15.5" y2="10" stroke="var(--tan)" stroke-width="1.2"/></svg>
      www.oaklanedigging.com
    </li>
  </ul>

  <div class="front-band"></div>
  <div class="front-stripe front-stripe--one"></div>
  <div class="front-stripe front-stripe--two"></div>
  <p class="services">Would also like to include Buyer, Broker, Consultant and Appraiser</p>
</section>

<section class="card card--back" aria-label="Business card back">
  <div class="back-art" role="img" aria-label="Faded illustration of a pin-up miner seated on an ore cart"></div>
  <svg class="corner-bracket back-bracket" width="70" height="75" viewBox="0 0 70 75" aria-hidden="true">
    <polyline points="2,0 2,73 70,73" fill="none" stroke="var(--tan)" stroke-width="3"/>
  </svg>

  <div class="name-pill">
    <div class="identity__name">Walter Brennick's</div>
    <div class="identity__company">Oak Lane Digging Co</div>
  </div>

  <div class="web-box">
    <svg viewBox="0 0 20 20" aria-hidden="true"><circle cx="10" cy="10" r="9.5" fill="var(--tan)"/><circle cx="10" cy="10" r="5.5" fill="none" stroke="var(--brown)" stroke-width="1.2"/><ellipse cx="10" cy="10" rx="2.3" ry="5.5" fill="none" stroke="var(--brown)" stroke-width="1.2"/><line x1="4.5" y1="10" x2="15.5" y2="10" stroke="var(--brown)" stroke-width="1.2"/></svg>
    www.oaklanedigging.com.
  </div>
</section>

</body>
</html>
```